Classic Personal Business Card in Regatta Dane Whitcomb Style (Horizontal - Raised Ink)

If you ever seen a Dane Whitcomb Regatta shirt, you will know that the signature of that shirt is small monogrammed icon on the left pocket. I envision my personal business card using some of these elements. I am in the oil exploration industry, which is very conservative and I want a card that looks great but still reflects that classic conservatism. I specifically do land management work, which means I determine who owns mineral rights, I lease those rights for larger companies to then drill for crude oil and natural gas

1. I have designed a small logo (which definitely could use some help) that I would like to be pretty small, centered in the middle of the card, and near the top of the card (color - navy blue or similar) Please feel free to make this logo infinitely better. However, I am not looking for anything abstract/

2. I want my name and designation (Morgan D. Hartwell, RPL) centered in the middle of the card. As far as font, I'm looking for a classic, strong (almost masculine) cursive font (I realize masculine + cursive is a little oxymoronic) and I would like it to the color to be Gold.

3. I would like my name (see above) to sit on top of a thin, centered navy blue (or similar) line as if it were almost a signature on a line. I want the lower-case letters that normally would dip below the line (which is y and p in my case) to do the same. I'll attach an example to help illustrate what I mean.

4. The rest of the card is my contact information. Because I am shoot for a more centered and balance look, I would like the placement of my contact information to also be centered and balance. Font should be a very classic, professional font. My first inclination is to use black for the color but I'm open to other suggestions.

Contact information:

Phone: (555) 014-2387
Email: mdhartwl@qovantri.com

Important Note: My hope is to have these printed with Raised Ink on High Quality High Quality Card Stock so it must conform to this Necessity.

Project Deadline Extended Reason: I am having major internet trouble. So I am not able to look at the submissions and provide feedback in a timely fashion. Also, it is difficult to access the site from just my phone. Added Saturday, November 22, 2014

Target Market(s)

US Oil Executives

Industry/Entity Type

Conservative

Contact Information for Business Card

I've posted a new logo that needs some clean up and a new idea for the top and bottom border of the card. I would like the logo to be centered in the top border with a white barrier on either side between the logo and the border. I've also posted color codes below.

Thanks

Requirements
Must have
• Color Codes:
• Blue: R - 0 G - 0 B - 102
• Gold R - 102 G - 102 B - 0

```html
<!DOCTYPE html>
<html lang="en">
<head>
<meta charset="utf-8">
<title>Morgan D. Hartwell, RPL — Business Card</title>
<link rel="stylesheet" href="https://fonts.googleapis.com/css2?family=Didact+Gothic&display=swap">
<style>
  :root {
    --navy: #000066;
    --navy-soft: #3b3b8a;
    --ink: #1c1c1c;
    --ink-soft: #2a2a2a;
    --paper: #f1f1f1;
    --paper-shade: #e2e2e2;
    --backdrop: #d8d5cf;
  }
  * { margin: 0; padding: 0; box-sizing: border-box; }
  html, body {
    width: 1200px;
    height: 1000px;
    overflow: hidden;
    background: var(--backdrop);
    font-family: "Didact Gothic", "Century Gothic", sans-serif;
  }
  .business-card {
    position: absolute;
    left: 100px;
    top: 214px;
    width: 1000px;
    height: 572px;
    background: radial-gradient(ellipse at 35% 40%, #fafafa 0%, var(--paper) 45%, var(--paper-shade) 100%);
    box-shadow: 0 10px 30px rgba(0,0,0,0.18);
    overflow: hidden;
  }
  .top-band {
    position: absolute;
    left: 0; top: 0;
    width: 100%;
    height: 14px;
    background: var(--navy);
  }
  .emblem {
    position: absolute;
    left: 50%;
    top: 52px;
    width: 124px;
    height: 124px;
    margin-left: -62px;
    border-radius: 50%;
    border: 1.5px solid var(--navy-soft);
    background: #ffffff;
    display: flex;
    align-items: center;
    justify-content: center;
    text-align: center;
  }
  .emblem-name {
    color: var(--navy);
    font-size: 17px;
    line-height: 1.2;
    letter-spacing: 0.5px;
  }
  .identity {
    position: absolute;
    left: 0;
    top: 262px;
    width: 100%;
    text-align: center;
  }
  .holder-name {
    font-size: 60px;
    color: var(--ink);
    font-weight: 400;
    letter-spacing: 0.5px;
    line-height: 1;
  }
  .signature-line {
    display: inline-block;
    border-bottom: 2px solid var(--navy);
    padding-bottom: 2px;
  }
  .contact-list {
    list-style: none;
    margin-top: 22px;
    padding-left: 90px;
    font-size: 42px;
    color: var(--ink-soft);
    line-height: 1.35;
  }
</style>
</head>
<body>
  <main class="business-card">
    <div class="top-band"></div>
    <div class="emblem">
      <span class="emblem-name">Hartwell<br>Land</span>
    </div>
    <section class="identity">
      <h1 class="holder-name"><span class="signature-line">Morgan D. Hartwell</span>, RPL</h1>
      <ul class="contact-list">
        <li class="contact-phone">Phone: (555) 014-2387</li>
        <li class="contact-email">Email: mdhartwl@qovantri.com</li>
      </ul>
    </section>
  </main>
</body>
</html>
```